2024 Harwick Patrol Deputy's Statute Handbook

Cover, spine and back cover for our annual law manual. The overall size of the cover is 18.82 x 11 (with the .25 inch bleed it is 19.32 x 11.5) and the spine is 1.82 x 11 plus (1.82 x 11.5 with the bleed).
The book comes with a motor vehicle companion guide which will be 5" X 7" with spiral binding. The companion guide will have the same design with a slight twist related to motor vehicle law.

```html
<!DOCTYPE html>
<html lang="en">
<head>
<meta charset="utf-8">
<title>Harwick Patrol Deputy's Motor Vehicle Guide 2024 – Covers</title>
<link rel="stylesheet" href="https://fonts.googleapis.com/css2?family=Montserrat:wght@700;800&family=Mulish:wght@400;500&display=swap">
<style>
  :root {
    --stage: #b5bdc3;
    --ink-dark: #141414;
    --ink-mid: #3a3a3a;
    --paper: #f2f2f2;
    --gold: #f2b51e;
    --flag-red: #9a2a32;
    --flag-blue: #2b3f78;
    --flag-white: #e8e4e4;
  }
  * { box-sizing: border-box; margin: 0; padding: 0; }
  html, body { width: 1200px; height: 995px; overflow: hidden; }
  body { background: var(--stage); font-family: "Mulish", sans-serif; position: relative; }

  .cover {
    position: absolute; top: 203px; width: 428px; height: 599px; overflow: hidden;
    background: var(--ink-dark); color: var(--paper);
  }
  .cover--back { left: 163px; }
  .cover--front { left: 603px; }

  .scene-photo { position: absolute; inset: 0; }
  .cover--back .scene-photo {
    background: radial-gradient(ellipse at 50% 45%, #5a5a5a 0%, #2c2c2c 55%, #161616 100%);
  }
  .cover--front .scene-photo {
    background:
      radial-gradient(ellipse at 60% 60%, #6b6b6b 0%, #333 45%, #0e0e0e 80%),
      #111;
  }
  .flag-photo {
    position: absolute; top: 0; left: 0; width: 100%; height: 160px;
    background: linear-gradient(165deg, var(--flag-blue) 0%, var(--flag-blue) 8%, var(--flag-white) 14%, var(--flag-red) 30%, #7a1e26 55%, rgba(40,20,20,0) 78%);
  }
  .cover--front .flag-photo {
    height: 260px;
    background: linear-gradient(160deg, var(--flag-blue) 0%, var(--flag-white) 14%, var(--flag-red) 30%, #6e1c24 52%, rgba(20,20,20,0) 72%);
  }
  .base-band { position: absolute; left: 0; right: 0; bottom: 0; height: 40px; background: #050505; }

  .gold-rule { position: absolute; left: 50%; width: 44px; height: 1.5px; margin-left: -22px; background: var(--gold); }
  .gold-rule--top { top: 161px; }
  .gold-rule--bottom { top: 370px; }

  .blurb {
    position: absolute; top: 180px; left: 34px; right: 34px;
    font-size: 10.6px; line-height: 13px; letter-spacing: 0.9px; text-align: center; color: var(--paper);
  }

  .brand {
    position: absolute; display: flex; align-items: center; gap: 5px;
    font-family: "Mulish", sans-serif; font-weight: 500; color: #d6d6d6; letter-spacing: 1px;
  }
  .brand-dot { width: 10px; height: 10px; border-radius: 50%; background: #d6d6d6; }
  .cover--back .brand { top: 498px; left: 0; right: 0; justify-content: center; font-size: 12px; }
  .cover--back .year { position: absolute; top: 543px; left: 0; right: 0; text-align: center; font-size: 16px; letter-spacing: 1.5px; }

  .author { position: absolute; top: 20px; left: 0; right: 0; padding-left: 100px; font-size: 15px; letter-spacing: 2px; font-weight: 500; }
  .cover--front .year { position: absolute; top: 70px; right: 30px; font-size: 30px; letter-spacing: 2px; font-weight: 500; }

  .title { position: absolute; left: 66px; right: 30px; top: 422px; }
  .title-kicker { font-size: 14.5px; letter-spacing: 1.4px; font-weight: 500; white-space: nowrap; }
  .title-main {
    font-family: "Montserrat", sans-serif; font-weight: 800; color: var(--gold);
    font-size: 35px; line-height: 1; margin-top: 6px; letter-spacing: -0.5px; white-space: nowrap;
  }
  .title-row { display: flex; align-items: center; justify-content: space-between; margin-top: 4px; }
  .title-row .brand { position: static; font-size: 10px; flex-direction: column; gap: 3px; }
  .title-guide {
    font-family: "Montserrat", sans-serif; font-weight: 800; color: var(--gold);
    font-size: 70px; line-height: 0.9; letter-spacing: -1px;
  }
</style>
</head>
<body>
  <section class="cover cover--back">
    <div class="scene-photo" role="img" aria-label="Blurred black-and-white night street scene"></div>
    <div class="flag-photo" role="img" aria-label="Draped American flag across the top corner"></div>
    <span class="gold-rule gold-rule--top"></span>
    <p class="blurb">This motor vehicle guide is the ultimate cruiser companion! It has everything a Harwick Patrol Deputy needs to know when enforcing motor vehicle laws and rules, from minor violations like defective equipment, to more complex areas such as international operators, to serious offenses such as motor vehicle homicide; everything is covered in an easy to understand format. It includes arrest powers, fine amounts, as well as the laws involving vehicle impoundments, exit orders and even motor vehicle searches. It is the only manual of its kind actually created by a working deputy (and attorney). It is the only motor vehicle cruiser guide you will need!</p>
    <span class="gold-rule gold-rule--bottom"></span>
    <div class="brand"><span class="brand-dot"></span>CORRIGAN</div>
    <p class="year">2024</p>
  </section>

  <section class="cover cover--front">
    <div class="scene-photo" role="img" aria-label="Black-and-white night scene of police cruisers with a gavel overlay"></div>
    <div class="flag-photo" role="img" aria-label="Draped American flag across the top of the cover"></div>
    <div class="base-band"></div>
    <p class="author">Daniel R. Corrigan, Esq.</p>
    <p class="year">2024</p>
    <div class="title">
      <p class="title-kicker">HARWICK PATROL DEPUTY'S</p>
      <h1 class="title-main">MOTOR VEHICLE</h1>
      <div class="title-row">
        <div class="brand"><span class="brand-dot"></span>CORRIGAN</div>
        <span class="title-guide">GUIDE</span>
      </div>
    </div>
  </section>
</body>
</html>
```